Welbourne Dental, P.C. New stationary and business card for modern Dental Office

We need a new stationary/envelope/business card design using our newly designed logo. We are looking for an upscale look. Our new logo is used on our signage, using black as the background and white for the lettering. We would like the stationary to have black, white, possible greys or silver. We are looking for a letterhead, envelope, and business card design for three different employees, as well as a 4th card, same design, but just general with no employee name.

Project Deadline Extended
Reason: We began this project in the middle of our move into our new office. Things got pretty hectic and we just didn't have the time to go through designs. We now settled in and finally eliminated the designs that didn't work for us. We would like to extend the project another 5 days, and then finalize our decision. Most of the submissions showed business cards alone, with no stationary designs. Our original request was for stationary and business cards. Please keep this in mind.

Target Market(s)

Dental patients expecting high quality, cosmetic dentistry

Industry/Entity Type

Business

Contact Information for Business Card

Will need a design using our logo. All cards will be the same, other than that one card will have Office Managers name, One for the Doctor, Hygienist,
1. Office Manager - Marisol Dubrovka
2. Hygienist - Kayleigh Morrow
3. Gordon T. Welbourne, D.D.S.
4. One general one with no staff names

Font styles to use
Other font styles liked:
• see upload

Colors
000000
1b1b1b
757575
c9c9c9
e8e8e8
ffffff

Requirements
Must have
• -Logo
• -Phone number (718)555-0193
• -Address: 4352 63rd Ave
• Lower Level
• Brooklyn, NY 11290

```html
<!DOCTYPE html>
<html lang="en">
<head>
<meta charset="utf-8">
<title>Welbourne Dental, P.C. — Business Card</title>
<link href="https://fonts.googleapis.com/css2?family=Marcellus&family=Open+Sans:wght@400;600&display=swap" rel="stylesheet">
<style>
  :root {
    --stage: #ececec;
    --card-white: #ffffff;
    --card-dark: #3a3332;
    --band-grey: #d9d5d2;
    --logo-warm: #c9c2bd;
    --text-light: #ffffff;
    --shadow: rgba(0, 0, 0, 0.18);
  }
  * { box-sizing: border-box; margin: 0; padding: 0; }
  html, body {
    width: 1200px; height: 900px; overflow: hidden;
    background: var(--stage);
  }
  .canvas { position: relative; width: 1200px; height: 900px; }

  .card {
    position: absolute;
    overflow: hidden;
    box-shadow: 0 6px 18px var(--shadow);
  }

  /* Front */
  .card-front {
    left: 78px; top: 34px; width: 588px; height: 363px;
    background: var(--card-white);
  }
  .card-front .bands { position: absolute; inset: 0; }

  .brand {
    position: absolute;
    display: flex; align-items: center; gap: 14px;
    font-family: "Marcellus", serif;
    white-space: nowrap;
  }
  .card-front .brand {
    left: 140px; top: 72px;
    font-size: 32px; color: var(--logo-warm);
  }
  .brand-dot {
    display: inline-block; width: 22px; height: 22px;
    border-radius: 50%;
    background: currentColor;
  }

  .contact {
    position: absolute;
    font-family: "Open Sans", sans-serif;
    color: var(--text-light);
    font-size: 14px; line-height: 21px;
    text-align: right;
  }
  .contact-phone {
    right: 306px; top: 257px;
    display: flex; align-items: center; gap: 7px;
  }
  .contact-phone svg { width: 12px; height: 12px; fill: var(--text-light); }
  .contact-address { right: 306px; top: 290px; }

  .person {
    position: absolute; left: 322px; top: 272px;
    font-family: "Open Sans", sans-serif;
    color: var(--text-light);
  }
  .person-name { font-size: 20px; font-weight: 600; line-height: 28px; }
  .person-title { font-size: 14px; line-height: 20px; }

  /* Back */
  .card-back {
    left: 388px; top: 505px; width: 567px; height: 352px;
    background: var(--card-dark);
  }
  .card-back .brand {
    right: 40px; bottom: 76px;
    font-size: 30px; color: var(--text-light);
  }
</style>
</head>
<body>
<main class="canvas">

  <section class="card card-front" aria-label="Business card front">
    <svg class="bands" width="588" height="363" viewBox="0 0 588 363" aria-hidden="true">
      <polygon points="0,198 410,198 382,226 0,226" fill="var(--band-grey)"/>
      <polygon points="0,232 384,232 418,194 588,194 588,363 0,363" fill="var(--card-dark)"/>
    </svg>

    <div class="brand">Welbourne Dental, P.C. <span class="brand-dot"></span></div>

    <div class="contact contact-phone">
      <span>718 555-0193</span>
      <svg viewBox="0 0 24 24" aria-hidden="true"><path d="M6.6 10.8a15.1 15.1 0 0 0 6.6 6.6l2.2-2.2a1 1 0 0 1 1-.25 11.4 11.4 0 0 0 3.6.57 1 1 0 0 1 1 1V20a1 1 0 0 1-1 1A17 17 0 0 1 3 4a1 1 0 0 1 1-1h3.5a1 1 0 0 1 1 1c0 1.25.2 2.45.57 3.57a1 1 0 0 1-.25 1z"/></svg>
    </div>
    <address class="contact contact-address" style="font-style:normal">
      4352 63rd Ave Lower Level<br>
      Brooklyn, NY 11290
    </address>

    <div class="person">
      <p class="person-name">Daniel Ferrante</p>
      <p class="person-title">Managing Director</p>
    </div>
  </section>

  <section class="card card-back" aria-label="Business card back">
    <div class="brand">Welbourne Dental, P.C. <span class="brand-dot"></span></div>
  </section>

</main>
</body>
</html>
```